Copper Lantern Banner Design for Conference

Design for a vertical retractable banner. Requirements are :
1. Use the attached PDF that shows the text content, logos and rough layout.
2. Use the logos in the attached AI files
3. Use the attached FramoLens image in the design
4. Included the design for one of our existing flyers in case useful
5. Use the corporate colours (Red and Black)
6. Design dimensions : 2000mm high x 820mm wide
7. 300 DPI

To meet a printing deadline I need the designs completed very quickly - 2 days (by COB Tuesday 29th August)

ec1f27

• Design dimensions : 2000mm high x 820mm wide

```html
<!DOCTYPE html>
<html lang="en">
<head>
<meta charset="utf-8">
<title>Copper Lantern – Conference Banner</title>
<link rel="stylesheet" href="https://fonts.googleapis.com/css2?family=Montserrat:wght@800&family=Arimo:wght@400&display=swap">
<style>
  :root {
    --red: #ec1f27;
    --navy: #141c38;
    --white: #ffffff;
    --frame: #3a3a3a;
    --photo-light: #e9ece6;
    --photo-wood: #c99a63;
    --photo-skin: #b98b72;
    --panel-top: #ffffff;
    --panel-bottom: #bfe9f3;
    --pill-violet: #5a3cc6;
    --pill-blue: #2f8fd8;
    --pill-teal: #3fc6a2;
    --pill-orange: #f47b20;
    --pill-crimson: #ee2f4a;
    --pill-magenta: #e2309c;
    --pill-navy: #1b2856;
    --pill-steel: #34508c;
    --connector: #cfd8de;
  }
  html, body {
    margin: 0;
    padding: 0;
    width: 1200px;
    height: 2906px;
    overflow: hidden;
    background: var(--white);
  }
  .banner {
    position: relative;
    width: 1200px;
    height: 2906px;
    box-sizing: border-box;
    border: 2px solid var(--frame);
    background: var(--white);
    overflow: hidden;
  }
  .brand {
    position: absolute;
    left: 70px;
    top: 210px;
    display: flex;
    align-items: center;
    gap: 40px;
  }
  .brand-dot {
    width: 220px;
    height: 220px;
    border-radius: 50%;
    background: var(--red);
  }
  .brand-name {
    font-family: "Montserrat", sans-serif;
    font-weight: 800;
    font-size: 72px;
    letter-spacing: 1px;
    color: var(--navy);
    white-space: nowrap;
  }
  .hero {
    position: absolute;
    left: 0;
    top: 0;
  }
  .headline {
    position: absolute;
    left: 0;
    width: 1200px;
    top: 1320px;
    margin: 0;
    text-align: center;
    font-family: "Arimo", sans-serif;
    font-weight: 400;
    font-size: 80px;
    line-height: 110px;
    color: var(--navy);
    letter-spacing: 1px;
  }
  .services {
    position: absolute;
    left: 58px;
    top: 1725px;
    width: 1105px;
    height: 1105px;
    background: linear-gradient(180deg, var(--panel-top) 0%, #f3fbfd 45%, var(--panel-bottom) 100%);
  }
  .diagram {
    position: absolute;
    left: 0;
    top: 0;
  }
  .tagline {
    position: absolute;
    left: 87px;
    top: 1900px;
    width: 368px;
    height: 368px;
    display: flex;
    align-items: center;
    justify-content: center;
    text-align: center;
    font-family: "Arimo", sans-serif;
    font-size: 50px;
    line-height: 60px;
    color: var(--red);
  }
  .service-label {
    position: absolute;
    right: 110px;
    text-align: right;
    font-family: "Arimo", sans-serif;
    font-size: 33px;
    line-height: 44px;
    color: var(--white);
    text-transform: uppercase;
  }
  .label-lifecycle { top: 1762px; }
  .label-integration { top: 2016px; }
  .label-custom { top: 2258px; }
</style>
</head>
<body>
<div class="banner">

  <div class="brand">
    <div class="brand-dot"></div>
    <div class="brand-name">COPPER LANTERN</div>
  </div>

  <svg class="hero" width="1200" height="1300" viewBox="0 0 1200 1300">
    <defs>
      <linearGradient id="photo-tones" x1="0" y1="0" x2="1" y2="1">
        <stop offset="0" stop-color="var(--photo-light)"/>
        <stop offset="0.45" stop-color="var(--photo-wood)"/>
        <stop offset="0.75" stop-color="var(--photo-skin)"/>
        <stop offset="1" stop-color="var(--photo-light)"/>
      </linearGradient>
    </defs>
    <g role="img" aria-label="FramoLens photograph: hands arranging wooden blocks in rising rows">
      <polygon points="417,459 1128,459 775,1086" fill="url(#photo-tones)"/>
      <polygon points="78,1231 442,616 805,1231" fill="url(#photo-tones)"/>
    </g>
    <polygon class="accent-triangle" points="616,397 93,1260 1140,1260" fill="none" stroke="var(--red)" stroke-width="3"/>
  </svg>

  <h1 class="headline">SOFTWARE SOLUTION<br>DESIGN AND<br>DEVELOPMENT</h1>

  <div class="services"></div>

  <svg class="diagram" width="1200" height="2906" viewBox="0 0 1200 2906">
    <defs>
      <linearGradient id="pill-lifecycle" x1="0" y1="0" x2="1" y2="0">
        <stop offset="0" stop-color="var(--pill-violet)"/>
        <stop offset="0.55" stop-color="var(--pill-blue)"/>
        <stop offset="1" stop-color="var(--pill-teal)"/>
      </linearGradient>
      <linearGradient id="pill-integration" x1="0" y1="0" x2="1" y2="0">
        <stop offset="0" stop-color="var(--pill-orange)"/>
        <stop offset="0.5" stop-color="var(--pill-crimson)"/>
        <stop offset="1" stop-color="var(--pill-magenta)"/>
      </linearGradient>
      <linearGradient id="pill-custom" x1="0" y1="0" x2="1" y2="0">
        <stop offset="0" stop-color="var(--pill-navy)"/>
        <stop offset="1" stop-color="var(--pill-steel)"/>
      </linearGradient>
      <radialGradient id="tagline-disc" cx="0.45" cy="0.4" r="0.6">
        <stop offset="0.6" stop-color="#ffffff"/>
        <stop offset="1" stop-color="#bfe6f1"/>
      </radialGradient>
      <radialGradient id="floor-shadow" cx="0.5" cy="0.5" r="0.5">
        <stop offset="0" stop-color="#9fb3bc" stop-opacity="0.6"/>
        <stop offset="1" stop-color="#9fb3bc" stop-opacity="0"/>
      </radialGradient>
    </defs>

    <ellipse cx="610" cy="2445" rx="460" ry="10" fill="url(#floor-shadow)"/>

    <!-- connector arc and leads -->
    <path d="M426 1886 Q 560 2096 426 2307" fill="none" stroke="var(--connector)" stroke-width="8"/>
    <line x1="426" y1="1886" x2="560" y2="1840" stroke="var(--connector)" stroke-width="6"/>
    <line x1="520" y1="2080" x2="560" y2="2060" stroke="var(--connector)" stroke-width="6"/>
    <line x1="426" y1="2307" x2="560" y2="2302" stroke="var(--connector)" stroke-width="6"/>
    <circle cx="426" cy="1886" r="19" fill="#e6e9f5" stroke="#8a86d0" stroke-width="6"/>
    <circle cx="520" cy="2080" r="19" fill="#fbe6ea" stroke="var(--pill-orange)" stroke-width="6"/>
    <circle cx="426" cy="2307" r="19" fill="#e1e5ee" stroke="var(--pill-steel)" stroke-width="6"/>

    <!-- tagline disc -->
    <circle cx="271" cy="2084" r="190" fill="#dff3f8"/>
    <circle cx="271" cy="2084" r="176" fill="url(#tagline-disc)" stroke="#d4edf4" stroke-width="4"/>

    <!-- pills -->
    <rect x="533" y="1739" width="611" height="180" rx="90" fill="url(#pill-lifecycle)"/>
    <rect x="548" y="1752" width="581" height="154" rx="77" fill="none" stroke="#ffffff" stroke-opacity="0.35" stroke-width="3"/>
    <rect x="533" y="1977" width="611" height="165" rx="82" fill="url(#pill-integration)"/>
    <rect x="548" y="1990" width="581" height="139" rx="70" fill="none" stroke="#ffe36b" stroke-opacity="0.5" stroke-width="3"/>
    <rect x="533" y="2210" width="611" height="184" rx="92" fill="url(#pill-custom)"/>
    <rect x="548" y="2223" width="581" height="158" rx="79" fill="none" stroke="#ffffff" stroke-opacity="0.3" stroke-width="3"/>

    <!-- icon discs -->
    <circle cx="620" cy="1829" r="60" fill="#eef0f4" stroke="#ffffff" stroke-width="6"/>
    <circle cx="620" cy="2059" r="58" fill="#eef0f4" stroke="#ffffff" stroke-width="6"/>
    <circle cx="620" cy="2302" r="60" fill="#eef0f4" stroke="#ffffff" stroke-width="6"/>

    <!-- gear icon -->
    <g fill="var(--navy)">
      <circle cx="608" cy="1838" r="16"/>
      <g stroke="var(--navy)" stroke-width="8">
        <line x1="608" y1="1814" x2="608" y2="1862"/>
        <line x1="584" y1="1838" x2="632" y2="1838"/>
        <line x1="591" y1="1821" x2="625" y2="1855"/>
        <line x1="625" y1="1821" x2="591" y2="1855"/>
      </g>
      <circle cx="608" cy="1838" r="6" fill="#eef0f4"/>
      <circle cx="638" cy="1815" r="10"/>
      <g stroke="var(--navy)" stroke-width="5">
        <line x1="638" y1="1801" x2="638" y2="1829"/>
        <line x1="624" y1="1815" x2="652" y2="1815"/>
      </g>
      <circle cx="638" cy="1815" r="4" fill="#eef0f4"/>
    </g>

    <!-- megaphone icon -->
    <g fill="var(--navy)">
      <rect x="594" y="2047" width="14" height="26" rx="2"/>
      <polygon points="610,2047 642,2030 642,2090 610,2073"/>
      <rect x="600" y="2073" width="9" height="16"/>
    </g>

    <!-- chat icon -->
    <g>
      <ellipse cx="620" cy="2298" rx="32" ry="25" fill="var(--navy)"/>
      <polygon points="598,2312 592,2330 614,2318" fill="var(--navy)"/>
      <circle cx="607" cy="2298" r="4" fill="#ffffff"/>
      <circle cx="620" cy="2298" r="4" fill="#ffffff"/>
      <circle cx="633" cy="2298" r="4" fill="#ffffff"/>
    </g>
  </svg>

  <div class="tagline">Your<br>Intellect,<br>Our<br>Solutions</div>

  <div class="service-label label-lifecycle">Software<br>Development<br>Lifecycle Automation</div>
  <div class="service-label label-integration">Systems<br>Integration</div>
  <div class="service-label label-custom">Custom Business<br>Solutions</div>

</div>
</body>
</html>
```